Supplment jar label design (full label)

Hydration (blue) 300g –700ml jar, label size: 10 cm x 27 cm
make label for Kora Vital supps
needs to be full blown label that fits size I noted above
with all claims in attached doc
see attached product info and claims
see QDL & Ember attached as example of similar to what I want
carbon fibre background on label
I have also attached label example this is how i expect to receive designs
where is states SKU on label needs to be in colour above
needs files to able to customise with other SKUs in future
please message me if you have questions
Hydration

```html
<!DOCTYPE html>
<html lang="en">
<head>
<meta charset="utf-8">
<title>Kora Vital Hydration – Jar Label</title>
<link href="https://fonts.googleapis.com/css2?family=Montserrat:wght@400;500;600;700;800&family=Poppins:wght@400;500;600;700&display=swap" rel="stylesheet">
<style>
  :root {
    --page-bg: #d6d7d9;
    --label-dark: #0d0d0e;
    --carbon-a: #2b2625;
    --carbon-b: #141213;
    --tan-light: #b4a79c;
    --tan-dark: #3f3027;
    --blue-light: #6d8fe6;
    --blue: #4a6fd0;
    --blue-deep: #2f4fc4;
    --green: #3f7a58;
    --panel-brown: #4a3a30;
    --white: #ffffff;
    --muted: #d9d4cf;
  }
  * { box-sizing: border-box; margin: 0; padding: 0; }
  html, body { width: 1200px; height: 857px; overflow: hidden; }
  body { background: var(--page-bg); font-family: "Poppins", sans-serif; color: var(--white); position: relative; }

  .label {
    position: absolute; left: 40px; top: 221px; width: 1120px; height: 415px;
    background: linear-gradient(90deg, var(--carbon-a) 0%, var(--carbon-b) 24%, var(--label-dark) 50%, var(--carbon-b) 76%, var(--carbon-a) 100%);
    border-radius: 6px; overflow: hidden;
  }
  .carbon-texture {
    position: absolute; inset: 0;
    background:
      radial-gradient(ellipse at 15% 30%, rgba(90,78,72,.35) 0%, rgba(90,78,72,0) 45%),
      radial-gradient(ellipse at 85% 70%, rgba(90,78,72,.3) 0%, rgba(90,78,72,0) 45%),
      linear-gradient(180deg, rgba(255,255,255,.04) 0%, rgba(0,0,0,.12) 100%);
  }
  .panel { position: absolute; top: 0; height: 100%; }

  /* Left: directions */
  .panel-directions { left: 0; width: 270px; padding: 60px 28px 0 30px; font-size: 10px; line-height: 1.55; color: var(--muted); }
  .panel-directions h3 { font-family: "Montserrat", sans-serif; font-weight: 700; font-size: 13px; color: var(--white); letter-spacing: 1px; margin-bottom: 8px; }
  .panel-directions p { margin-bottom: 14px; }
  .warning-box { border: 1px solid var(--white); border-radius: 6px; padding: 10px 12px; margin-bottom: 16px; color: var(--white); }

  /* Front */
  .panel-front { left: 270px; width: 580px; }
  .front-shape { position: absolute; left: 0; top: 0; }
  .claim-icons { position: absolute; left: 55px; top: 0; width: 80px; height: 100%; }
  .claim { position: absolute; left: 0; width: 80px; text-align: center; }
  .claim svg { display: block; margin: 0 auto 6px; }
  .claim span { display: block; font-family: "Montserrat", sans-serif; font-size: 5px; line-height: 1.3; letter-spacing: .3px; color: var(--white); }
  .claim-dot { position: absolute; left: 38px; width: 4px; height: 4px; background: var(--white); }

  .brand-name { position: absolute; left: 152px; top: 58px; font-family: "Montserrat", sans-serif; font-weight: 800; font-size: 40px; line-height: .95; color: var(--white); letter-spacing: -1px; }
  .origin-badge { position: absolute; left: 418px; top: 58px; width: 62px; height: 54px; background: var(--green); border-radius: 22px 26px 24px 18px; }

  .product-name {
    position: absolute; left: 150px; top: 172px; font-family: "Montserrat", sans-serif; font-weight: 800; font-size: 50px; letter-spacing: -1px;
    background: linear-gradient(90deg, var(--blue-light) 0%, var(--blue-deep) 35%, var(--blue-deep) 65%, var(--blue) 100%);
    -webkit-background-clip: text; background-clip: text; color: transparent;
  }
  .product-type { position: absolute; left: 152px; top: 238px; font-family: "Montserrat", sans-serif; font-weight: 500; font-size: 12.5px; letter-spacing: 4.2px; }
  .flavour { position: absolute; left: 152px; top: 300px; font-family: "Montserrat", sans-serif; font-size: 10px; letter-spacing: 2.4px; }
  .size-pill { position: absolute; left: 152px; top: 318px; display: flex; border: 2px solid var(--white); border-radius: 7px; overflow: hidden; font-family: "Poppins", sans-serif; font-size: 14px; }
  .size-pill .weight { background: #3a3a3a; font-weight: 600; padding: 2px 8px; border-radius: 5px; }
  .size-pill .volume { background: var(--white); color: #1a1a1a; padding: 2px 7px; }

  .mineral { position: absolute; left: 393px; width: 92px; height: 31px; background: var(--blue); padding: 2px 0 0 12px; line-height: 1; }
  .mineral b { font-family: "Poppins", sans-serif; font-weight: 700; font-size: 14px; }
  .mineral b small { font-size: 10px; }
  .mineral span { display: block; font-family: "Montserrat", sans-serif; font-size: 8px; margin-top: 1px; }

  /* Right: nutrition */
  .panel-info { left: 850px; width: 270px; padding: 0 18px; }
  .nutrition { position: absolute; left: 16px; top: 56px; width: 236px; background: var(--panel-brown); border-radius: 10px; padding: 10px 14px 8px; }
  .nutrition h3 { font-family: "Poppins", sans-serif; font-weight: 700; font-size: 17px; line-height: 1.1; }
  .nutrition .serves { font-size: 7px; color: var(--muted); margin: 2px 0 6px; }
  .nutrition table { width: 100%; border-collapse: collapse; font-size: 6.5px; }
  .nutrition th { text-align: right; font-weight: 600; padding-bottom: 2px; border-bottom: 1.5px solid var(--white); }
  .nutrition th:first-child { text-align: left; }
  .nutrition td { padding: 1.5px 0; border-bottom: .5px solid rgba(255,255,255,.6); }
  .nutrition td + td { text-align: right; }
  .nutrition .note { font-size: 5px; font-style: italic; margin-top: 4px; }
  .ingredients { position: absolute; left: 16px; top: 330px; width: 236px; font-size: 7px; line-height: 1.5; color: var(--muted); }
  .ingredients strong { color: var(--white); display: block; margin-bottom: 1px; }
</style>
</head>
<body>
<main class="label">
  <div class="carbon-texture" role="img" aria-label="Carbon fibre hexagon texture across the label background"></div>

  <section class="panel panel-directions">
    <h3>DIRECTIONS</h3>
    <p>Mix one scoop (10g) with 700ml of cold water. Shake well before use.</p>
    <div class="warning-box">Not suitable for children under 15 years or pregnant women.</div>
    <p>Store below 25°C in a cool, dry place. Keep sealed after opening the product.</p>
    <p>Formulated to support hydration and an active lifestyle as part of a balanced diet and exercise program.</p>
  </section>

  <section class="panel panel-front">
    <svg class="front-shape" width="580" height="415" viewBox="0 0 580 415" aria-hidden="true">
      <defs>
        <linearGradient id="tanFade" x1="0" y1="0" x2="1" y2="0">
          <stop offset="0" stop-color="#b4a79c"/>
          <stop offset=".55" stop-color="#6b5848"/>
          <stop offset="1" stop-color="#3f3027"/>
        </linearGradient>
      </defs>
      <polygon points="55,25 402,25 310,152 135,152 135,415 55,415" fill="url(#tanFade)"/>
    </svg>

    <div class="claim-icons">
      <div class="claim" style="top:92px">
        <svg width="42" height="42" viewBox="0 0 42 42"><circle cx="21" cy="21" r="19" fill="none" stroke="#fff" stroke-width="2"/><line x1="8" y1="34" x2="34" y2="8" stroke="#fff" stroke-width="2"/><path d="M21 31V13M21 18l-5-3M21 23l-5-3M21 18l5-3M21 23l5-3" stroke="#fff" stroke-width="1.6" fill="none"/></svg>
        <span>GLUTEN FREE</span>
      </div>
      <div class="claim-dot" style="top:172px"></div>
      <div class="claim" style="top:188px">
        <svg width="42" height="42" viewBox="0 0 42 42"><circle cx="21" cy="21" r="19" fill="none" stroke="#fff" stroke-width="2"/><line x1="8" y1="34" x2="34" y2="8" stroke="#fff" stroke-width="2"/><rect x="15" y="15" width="12" height="15" fill="none" stroke="#fff" stroke-width="1.6"/></svg>
        <span>NO ADDED<br>ARTIFICIAL FLAVOUR,<br>COLOUR &amp; SWEETENER</span>
      </div>
      <div class="claim-dot" style="top:276px"></div>
      <div class="claim" style="top:292px">
        <svg width="42" height="42" viewBox="0 0 42 42"><circle cx="21" cy="21" r="19" fill="none" stroke="#fff" stroke-width="2"/><line x1="8" y1="34" x2="34" y2="8" stroke="#fff" stroke-width="2"/><path d="M18 10v18a3 3 0 0 0 6 0V10" fill="none" stroke="#fff" stroke-width="1.6"/></svg>
        <span>NO ADDED<br>SUGAR</span>
      </div>
    </div>

    <div class="brand-name">KORA<br>VITAL</div>
    <div class="origin-badge" aria-hidden="true"></div>

    <h1 class="product-name">HYDRATION</h1>
    <p class="product-type">SUPPLEMENT DRINK MIX</p>
    <p class="flavour">LEMON FLAVOUR</p>
    <div class="size-pill"><span class="weight">300g</span><span class="volume">700ml</span></div>

    <div class="mineral" style="top:266px"><b>1200<small>mg</small></b><span>SODIUM</span></div>
    <div class="mineral" style="top:304px"><b>250<small>mg</small></b><span>POTASSIUM</span></div>
    <div class="mineral" style="top:342px"><b>80<small>mg</small></b><span>MAGNESIUM</span></div>
  </section>

  <section class="panel panel-info">
    <div class="nutrition">
      <h3>Nutrition Information</h3>
      <p class="serves">Servings per pack: 30 &nbsp; Serving size: 10g</p>
      <table>
        <tr><th></th><th>Per serve</th><th>Per 100g</th></tr>
        <tr><td>Energy</td><td>42kJ</td><td>420kJ</td></tr>
        <tr><td>Protein</td><td>0g</td><td>0g</td></tr>
        <tr><td>Gluten</td><td>0g</td><td>0g</td></tr>
        <tr><td>Fat</td><td>0g</td><td>0g</td></tr>
        <tr><td>Total Saturated</td><td>0g</td><td>0g</td></tr>
        <tr><td>Carbohydrate</td><td>2.1g</td><td>21g</td></tr>
        <tr><td>Sugars</td><td>0g</td><td>0g</td></tr>
        <tr><td>Dietary Fibre</td><td>0g</td><td>0g</td></tr>
        <tr><td>Sodium</td><td>1200mg</td><td>12000mg</td></tr>
        <tr><td>Potassium</td><td>250mg</td><td>2500mg</td></tr>
        <tr><td>Calcium</td><td>60mg</td><td>600mg</td></tr>
        <tr><td>Magnesium</td><td>80mg</td><td>800mg</td></tr>
      </table>
      <p class="note">*Nutrition information is approximate.</p>
    </div>
    <div class="ingredients">
      <strong>Ingredients:</strong>
      Electrolyte Minerals (Sodium Chloride, Calcium Citrate, Magnesium Citrate), Food Acid (Citric Acid), Sweetener (Stevia), Natural Lemon Flavour.
    </div>
  </section>

</main>
</body>
</html>
```